Heron Freightlines needs Bussiness cards!

Our new trucking company needs business cards!
We need the same design with two different names and emails, everything else it's the same.
I have included our original logo so we can use it for the design.
Note: the logo to be used is the o e with the buffalo on the right side, next to the letters H and F.

Target Market(s)

Trucking, refrigerated transportation, freight

Industry/Entity Type

Business

Contact Information for Business Card

Card #1:
Marcus Tellwright
marcustellwright@heronfreightlines.example
1-844-555-0193
(956)555-0178
3817 W. Tarrow Ave.
Pharr, TX 78599
www.heronfreightlines.example

Card#2:
Orla Brennick
orla@heronfreightlines.example
1-844-555-0193
(956)555-0178
3817 W. Tarrow Ave.
Pharr, TX 78599
www.heronfreightlines.example

Font styles to use
Sans Serif

Colors
0655a3
ec1f27
ffffff

Requirements
Must have
• our logo
Nice to have
• roads on background,

```html
<!DOCTYPE html>
<html lang="en">
<head>
<meta charset="utf-8">
<title>Heron Freightlines — Business Cards</title>
<link href="https://fonts.googleapis.com/css2?family=Lato:wght@400;700;900&display=swap" rel="stylesheet">
<style>
  :root {
    --brand-blue: #0655a3;
    --brand-red: #ec1f27;
    --white: #ffffff;
    --text-grey: #4a4a4a;
    --backdrop: #e7e4e0;
    --mascot-blue: #c8d2e2;
    --mascot-peach: #f2d6c8;
  }
  * { margin: 0; padding: 0; box-sizing: border-box; }
  html, body { width: 1200px; height: 848px; overflow: hidden; }
  body {
    background: var(--backdrop);
    font-family: "Lato", Arial, sans-serif;
    position: relative;
  }
  .card {
    position: absolute;
    width: 547px;
    height: 291px;
    background: var(--white);
    border-radius: 16px;
    overflow: hidden;
    box-shadow: 0 2px 6px rgba(0,0,0,0.18);
  }
  .card--back-top { left: 28px; top: 110px; }
  .card--front-marcus { left: 627px; top: 110px; }
  .card--front-orla { left: 28px; top: 478px; }
  .card--back-bottom { left: 627px; top: 478px; }

  .mascot-area {
    position: absolute;
    left: 0; top: 28px;
    width: 545px; height: 230px;
    background:
      linear-gradient(90deg, var(--mascot-blue) 0%, var(--mascot-blue) 22%, var(--mascot-peach) 40%, rgba(242,214,200,0) 100%);
    border-radius: 40% 4% 60% 45% / 55% 10% 90% 50%;
    opacity: 0.75;
  }

  .wordmark {
    position: absolute;
    display: flex;
    align-items: center;
    gap: 8px;
    font-weight: 900;
    color: var(--brand-blue);
    white-space: nowrap;
    letter-spacing: -0.3px;
  }
  .wordmark__dot {
    width: 14px; height: 14px;
    border-radius: 50%;
    background: var(--brand-red);
    flex: none;
  }
  .card--back-top .wordmark,
  .card--back-bottom .wordmark { left: 168px; top: 138px; font-size: 27px; }
  .card--front-marcus .wordmark { left: 34px; top: 52px; font-size: 25px; }
  .card--front-orla .wordmark { left: 258px; top: 50px; font-size: 25px; }

  .back-url {
    position: absolute;
    left: 0; right: 0;
    top: 249px;
    text-align: center;
    font-size: 12.5px;
    font-weight: 700;
    color: var(--brand-blue);
  }

  .person-name {
    position: absolute;
    color: var(--brand-red);
    font-weight: 400;
  }
  .card--front-marcus .person-name { right: 38px; top: 84px; font-size: 21px; }
  .card--front-orla .person-name { left: 34px; top: 43px; font-size: 17px; }
  .person-title {
    position: absolute;
    left: 34px; top: 63px;
    font-size: 12.5px;
    color: var(--text-grey);
  }

  .address, .contact-list {
    position: absolute;
    font-size: 12.5px;
    line-height: 16.5px;
    color: var(--text-grey);
    list-style: none;
  }
  .card--front-marcus .address { right: 38px; top: 140px; text-align: right; }
  .card--front-marcus .contact-list { right: 38px; top: 193px; text-align: right; }
  .card--front-orla .address { left: 34px; top: 119px; line-height: 18.5px; }
  .card--front-orla .contact-list { left: 34px; top: 167px; }

  .contact-list li { display: flex; align-items: center; gap: 6px; }
  .card--front-marcus .contact-list li { justify-content: flex-end; flex-direction: row-reverse; }
  .contact-icon { width: 11px; height: 11px; flex: none; fill: var(--brand-blue); }

  .wave { position: absolute; left: 0; top: 0; width: 547px; height: 291px; }
  .front-url {
    position: absolute;
    left: 34px; top: 263px;
    font-size: 12px;
    color: var(--white);
  }
</style>
</head>
<body>

  <section class="card card--back-top">
    <div class="mascot-area" role="img" aria-label="Faint mascot illustration with speed streaks"></div>
    <div class="wordmark"><span class="wordmark__dot"></span>Heron Freightlines</div>
    <p class="back-url">www.heronfreightlines.example</p>
  </section>

  <section class="card card--front-marcus">
    <div class="wordmark"><span class="wordmark__dot"></span>Heron Freightlines</div>
    <h2 class="person-name">Marcus Tellwright</h2>
    <p class="address">3817 W. Tarrow Ave. Pharr<br>TX 78599</p>
    <ul class="contact-list">
      <li><svg class="contact-icon" viewBox="0 0 12 12"><path d="M2.5 0.5 L4.5 0.5 L5.5 3.3 L4 4.4 C4.7 6 6 7.3 7.6 8 L8.7 6.5 L11.5 7.5 L11.5 9.5 C11.5 10.6 10.6 11.5 9.5 11.5 C4.5 11.2 0.8 7.5 0.5 2.5 C0.5 1.4 1.4 0.5 2.5 0.5Z"/></svg>(956)555-0178</li>
      <li><svg class="contact-icon" viewBox="0 0 12 12"><path d="M3 0 H9 A1 1 0 0 1 10 1 V11 A1 1 0 0 1 9 12 H3 A1 1 0 0 1 2 11 V1 A1 1 0 0 1 3 0Z M3.2 1.5 V9.5 H8.8 V1.5Z"/></svg>1-844-555-0193</li>
      <li><svg class="contact-icon" viewBox="0 0 12 12"><path d="M0.5 2.5 H11.5 V9.5 H0.5Z M1.2 3 L6 6.4 L10.8 3Z" fill-rule="evenodd"/></svg>marcustellwright@heronfreightlines.example</li>
    </ul>
    <svg class="wave" viewBox="0 0 547 291" aria-hidden="true">
      <path d="M0 240 C150 212 300 276 547 252 L547 264 C300 287 150 226 0 252Z" fill="var(--brand-red)"/>
      <path d="M0 255 C150 230 300 285 547 266 L547 270 C300 289 150 235 0 259Z" fill="var(--brand-blue)"/>
      <path d="M0 263 C150 242 300 292 547 274 L547 291 L0 291Z" fill="var(--brand-blue)"/>
    </svg>
    <p class="front-url">www.heronfreightlines.example</p>
  </section>

  <section class="card card--front-orla">
    <h2 class="person-name">Orla Brennick</h2>
    <p class="person-title">President</p>
    <div class="wordmark"><span class="wordmark__dot"></span>Heron Freightlines</div>
    <p class="address">3817 W. Tarrow Ave.<br>Pharr, TX 78599</p>
    <ul class="contact-list">
      <li><svg class="contact-icon" viewBox="0 0 12 12"><path d="M2.5 0.5 L4.5 0.5 L5.5 3.3 L4 4.4 C4.7 6 6 7.3 7.6 8 L8.7 6.5 L11.5 7.5 L11.5 9.5 C11.5 10.6 10.6 11.5 9.5 11.5 C4.5 11.2 0.8 7.5 0.5 2.5 C0.5 1.4 1.4 0.5 2.5 0.5Z"/></svg>(956)555-0178</li>
      <li><svg class="contact-icon" viewBox="0 0 12 12"><path d="M3 0 H9 A1 1 0 0 1 10 1 V11 A1 1 0 0 1 9 12 H3 A1 1 0 0 1 2 11 V1 A1 1 0 0 1 3 0Z M3.2 1.5 V9.5 H8.8 V1.5Z"/></svg>1-844-555-0193</li>
      <li><svg class="contact-icon" viewBox="0 0 12 12"><path d="M0.5 2.5 H11.5 V9.5 H0.5Z M1.2 3 L6 6.4 L10.8 3Z" fill-rule="evenodd"/></svg>orla@heronfreightlines.example</li>
    </ul>
    <svg class="wave" viewBox="0 0 547 291" aria-hidden="true">
      <path d="M0 240 C150 212 300 276 547 252 L547 264 C300 287 150 226 0 252Z" fill="var(--brand-red)"/>
      <path d="M0 255 C150 230 300 285 547 266 L547 270 C300 289 150 235 0 259Z" fill="var(--brand-blue)"/>
      <path d="M0 263 C150 242 300 292 547 274 L547 291 L0 291Z" fill="var(--brand-blue)"/>
    </svg>
    <p class="front-url">www.heronfreightlines.example</p>
  </section>

  <section class="card card--back-bottom">
    <div class="mascot-area" role="img" aria-label="Faint mascot illustration with speed streaks"></div>
    <div class="wordmark"><span class="wordmark__dot"></span>Heron Freightlines</div>
    <p class="back-url">www.heronfreightlines.example</p>
  </section>

</body>
</html>
```